Round Label Sticker 2.5-3 inch diameter

We need a design for a sticker to distribute for more brand recognition and product outreach.
My company The Bright Plate Company Ltd. Specializes in working with people with diabetes. My products are made for diabetics because they have no added sugars, high in protein and fiber and each serving is lower than 5% daily value of carbohydrates.
I am a dietitian and my dad passed away from diabetes. I have created a growing food and beverage line that will give more joy into a diabetic's life while providing more food options that make them feel happy instead of guilty when they eat it.
I am teaching cooking classes to promote my products as well as doing exhibits and events. I want to give away a sticker to people that reads "I'm too sweet for sugar!" and somewhere on it would be my logo as well as my website info. www.brightplate.example
The sticker should make people smile and warm as well as draw interest to my product line.
Target Market(s)
Diabetes and people who do not want added sugars in their food
Industry/Entity Type
Food Store
Requirements
Must have
- my logo and website

```html
<!DOCTYPE html>
<html lang="en">
<head>
<meta charset="utf-8">
<title>Bright Plate – Round Sticker Designs</title>
<link href="https://fonts.googleapis.com/css2?family=Alegreya:ital,wght@0,700;1,400&display=swap" rel="stylesheet">
<style>
  :root {
    --purple: #5b2d8e;
    --white: #ffffff;
    --green: #4aa53a;
    --salmon: #ee9a88;
    --salmon-soft: #f9d9d0;
    --lavender-wash: #f4f0f9;
    --purple-wash: #643797;
    --check-light: #d9cdea;
    --check-dark: #6b43a0;
  }
  html, body {
    margin: 0;
    width: 1200px;
    height: 1200px;
    overflow: hidden;
    background: var(--white);
  }
  .sticker-sheet { display: block; width: 1200px; height: 1200px; }
  .slogan {
    font-family: "Alegreya", Georgia, serif;
    font-style: italic;
    font-weight: 400;
    font-size: 54px;
  }
  .web-address {
    font-family: "Alegreya", Georgia, serif;
    font-style: italic;
    font-weight: 400;
    font-size: 32px;
  }
  .brand-name {
    font-family: "Alegreya", Georgia, serif;
    font-weight: 700;
    font-size: 54px;
    text-anchor: middle;
  }
  .sticker--light .slogan,
  .sticker--light .web-address,
  .sticker--light .brand-name { fill: var(--purple); }
  .sticker--dark .slogan,
  .sticker--dark .web-address,
  .sticker--dark .brand-name { fill: var(--white); }
  .web-highlight { fill: var(--green); }
  .sticker--light .sticker-face { fill: var(--white); stroke: var(--purple); stroke-width: 4; }
  .sticker--dark .sticker-face { fill: var(--purple); }
  .sticker--light .picnic-corner { fill: url(#gingham-salmon); }
  .sticker--dark .picnic-corner { fill: url(#gingham-purple); }
  .sticker--light .treats-area { fill: var(--lavender-wash); }
  .sticker--dark .treats-area { fill: var(--purple-wash); }
</style>
</head>
<body>
<svg class="sticker-sheet" viewBox="0 0 1200 1200" xmlns="http://www.w3.org/2000/svg">
  <defs>
    <clipPath id="clip-light"><circle cx="312" cy="568" r="256"/></clipPath>
    <clipPath id="clip-dark"><circle cx="894" cy="566" r="257"/></clipPath>
    <linearGradient id="gingham-salmon" x1="0" y1="1" x2="1" y2="0">
      <stop offset="0" stop-color="var(--salmon)"/>
      <stop offset="0.5" stop-color="var(--salmon-soft)"/>
      <stop offset="1" stop-color="var(--salmon)"/>
    </linearGradient>
    <linearGradient id="gingham-purple" x1="0" y1="1" x2="1" y2="0">
      <stop offset="0" stop-color="var(--check-dark)"/>
      <stop offset="0.5" stop-color="var(--check-light)"/>
      <stop offset="1" stop-color="var(--check-dark)"/>
    </linearGradient>
    <path id="slogan-arc-light" d="M 109 514 A 210 210 0 0 1 515 514"/>
    <path id="web-arc-light" d="M 350 787 A 222 222 0 0 0 534 560"/>
    <path id="slogan-arc-dark" d="M 691 512 A 210 210 0 0 1 1097 512"/>
    <path id="web-arc-dark" d="M 932 785 A 222 222 0 0 0 1116 558"/>
  </defs>

  <g class="sticker sticker--light">
    <circle class="sticker-face" cx="312" cy="568" r="256"/>
    <g clip-path="url(#clip-light)">
      <polygon class="picnic-corner" points="-10,442 520,965 -10,965" role="img" aria-label="Salmon and white gingham tablecloth pattern"/>
    </g>
    <ellipse class="treats-area" cx="312" cy="590" rx="150" ry="135" role="img" aria-label="Faint line drawings of treats: kebab, pancakes, cheese, soup bowl, donut, pie, cupcake, croissant, candy jar and wrapped sweets"/>
    <text class="slogan"><textPath href="#slogan-arc-light" startOffset="0" textLength="530" lengthAdjust="spacing">I'm too sweet for sugar!</textPath></text>
    <text class="brand-name" x="312" y="575">Bright</text>
    <text class="brand-name" x="312" y="632">Plate</text>
    <text class="web-address"><textPath href="#web-arc-light" startOffset="0" textLength="316" lengthAdjust="spacingAndGlyphs">www.<tspan class="web-highlight">bright</tspan>plate.example</textPath></text>
  </g>

  <g class="sticker sticker--dark">
    <circle class="sticker-face" cx="894" cy="566" r="257"/>
    <g clip-path="url(#clip-dark)">
      <polygon class="picnic-corner" points="600,449 1000,881 1000,1000 600,1000" role="img" aria-label="Purple and white gingham tablecloth pattern"/>
    </g>
    <ellipse class="treats-area" cx="894" cy="588" rx="150" ry="135" role="img" aria-label="Faint line drawings of treats: kebab, pancakes, cheese, soup bowl, pie, cupcake, croissant, candy jar and wrapped sweets"/>
    <text class="slogan"><textPath href="#slogan-arc-dark" startOffset="0" textLength="530" lengthAdjust="spacing">I'm too sweet for sugar!</textPath></text>
    <text class="brand-name" x="894" y="573">Bright</text>
    <text class="brand-name" x="894" y="630">Plate</text>
    <text class="web-address"><textPath href="#web-arc-dark" startOffset="0" textLength="316" lengthAdjust="spacingAndGlyphs">www.<tspan class="web-highlight">bright</tspan>plate.example</textPath></text>
  </g>
</svg>
</body>
</html>
```